Stationary and Business Card for dental office
Velbrook Endodontics
Stationary and Business Card for dental office  - Health
Creative Brief
Use same font as used in my logo
use any font that is easy to read. should go with font in the logo
Professional
Miren T. Osbury, D.D.S.
418 Pelloway Court, Suite #1 Manteca, CA 95337
info@velbrookendo.example
www.velbrookendo.example
Business card should have 2 logos, one brown and gold one with a tooth image....that is my main logo. The second logo( the one that says pdrcertified member) which I have uploaded as well can be in a corner or anywhere on the card. basically it is your choice where it goes on the card. It does not have to be the same size as my main business logo. This second logo only needs to be on the business cards. it can be black and white or color. I will leave that decision to you so if you think the colored logo goes with my logo colors, then use that. If not then, use the black and white one. I will prefer it in color. Under my name on business card, please write the following in smaller font Practice Limited to Endodontics LETTER HEAD: deisgn does not need to have the second logo (pdrcertifeid member logo). It should have my main business logo ( gold and brown one) with business name and all the other info like address, phone, fax web/email. ENVELOPE: only main business logo with business name and address. Please do not include phone/fax/ email or any other logos on the envelope. Thank you.

```html
<!DOCTYPE html>
<html lang="en">
<head>
<meta charset="utf-8">
<title>Velbrook Endodontics — Business Card</title>
<link href="https://fonts.googleapis.com/css2?family=Michroma&family=Questrial&display=swap" rel="stylesheet">
<style>
  :root {
    --brown: #4a2c1c;
    --brown-deep: #3a2115;
    --gold: #c9a57a;
    --gold-light: #e3c9a3;
    --ink: #3b2a20;
    --paper: #ffffff;
    --stage: #d9d9d9;
  }
  html, body {
    margin: 0;
    width: 1200px;
    height: 901px;
    overflow: hidden;
    background: var(--stage);
  }
  .canvas {
    position: relative;
    width: 1200px;
    height: 901px;
    display: flex;
    align-items: center;
    justify-content: center;
    gap: 40px;
  }
  .card {
    position: relative;
    width: 540px;
    height: 309px;
    border-radius: 16px;
    overflow: hidden;
    font-family: "Questrial", sans-serif;
    box-shadow: 0 2px 6px rgba(0,0,0,.15);
  }
  /* back side */
  .card-back {
    background: radial-gradient(circle at 50% 40%, #5a3624 0%, var(--brown) 45%, var(--brown-deep) 100%);
  }
  .back-mark {
    position: absolute;
    top: 104px;
    left: 0;
    right: 0;
    display: flex;
    align-items: center;
    justify-content: center;
    gap: 14px;
  }
  .back-mark .dot {
    width: 62px;
    height: 62px;
    border-radius: 50%;
    background: var(--gold);
  }
  .back-mark .name {
    font-size: 24px;
    color: var(--gold-light);
    letter-spacing: 1px;
  }
  .back-web {
    position: absolute;
    left: 40px;
    bottom: 28px;
    font-size: 13px;
    letter-spacing: 4px;
    color: var(--gold-light);
  }
  /* front side */
  .card-front { background: var(--paper); }
  .front-waves { position: absolute; inset: 0; }
  .brand {
    position: absolute;
    top: 20px;
    left: 24px;
    display: flex;
    align-items: center;
    gap: 10px;
  }
  .brand .dot {
    width: 48px;
    height: 48px;
    border-radius: 50%;
    background: var(--brown);
  }
  .brand .name {
    font-size: 14px;
    color: var(--brown);
  }
  .practice {
    position: absolute;
    top: 78px;
    left: 24px;
    font-size: 10px;
    font-weight: bold;
    font-style: italic;
    color: var(--brown);
  }
  .doctor {
    position: absolute;
    top: 50px;
    right: 28px;
    font-family: "Michroma", sans-serif;
    font-size: 13px;
    color: var(--ink);
  }
  .contact {
    position: absolute;
    top: 98px;
    left: 24px;
    font-size: 13px;
    line-height: 16px;
    color: var(--ink);
  }
  .contact .address { margin-bottom: 8px; }
  .contact .row { display: flex; align-items: center; gap: 6px; }
  .contact .row svg { width: 12px; height: 12px; fill: var(--ink); }
  .contact .row .spacer { width: 12px; }
  .badge {
    position: absolute;
    right: 34px;
    bottom: 32px;
    width: 34px;
    height: 34px;
    border-radius: 50%;
    border: 2px solid var(--paper);
  }
</style>
</head>
<body>
<main class="canvas">
  <section class="card card-back" aria-label="Business card back">
    <div class="back-mark">
      <span class="dot"></span>
      <span class="name">Velbrook Endodontics</span>
    </div>
    <div class="back-web">www.velbrookendo.example</div>
  </section>

  <section class="card card-front" aria-label="Business card front">
    <svg class="front-waves" viewBox="0 0 540 309" preserveAspectRatio="none" aria-hidden="true">
      <path d="M0 200 C 150 250, 330 240, 540 140 L540 309 L0 309 Z" fill="var(--gold)"/>
      <path d="M0 214 C 150 262, 330 252, 540 154 L540 309 L0 309 Z" fill="var(--paper)"/>
      <path d="M0 226 C 150 270, 330 262, 540 166 L540 309 L0 309 Z" fill="var(--brown)"/>
    </svg>

    <div class="brand">
      <span class="dot"></span>
      <span class="name">Velbrook Endodontics</span>
    </div>
    <div class="practice">Practice Limited to Endodontics</div>
    <div class="doctor">Miren T. Osbury, D.D.S.</div>

    <div class="contact">
      <div class="address">418 Pelloway Court, Suite #7<br>Darrowfield, CA 95012</div>
      <div class="row">
        <svg viewBox="0 0 24 24"><path d="M6.6 10.8a15 15 0 0 0 6.6 6.6l2.2-2.2c.3-.3.7-.4 1-.2 1.1.4 2.3.6 3.6.6.6 0 1 .4 1 1V20c0 .6-.4 1-1 1A17 17 0 0 1 3 4c0-.6.4-1 1-1h3.5c.6 0 1 .4 1 1 0 1.3.2 2.5.6 3.6.1.3 0 .7-.2 1z"/></svg>
        <span>209-555-0142</span>
      </div>
      <div class="row">
        <svg viewBox="0 0 24 24"><path d="M6 3h12v5H6zM3 9h18v9h-3v3H6v-3H3zm5 6v4h8v-4z"/></svg>
        <span>209-555-0187</span>
      </div>
      <div class="row">
        <svg viewBox="0 0 24 24"><path d="M2 5h20v14H2zm2 2v.5l8 5 8-5V7z"/></svg>
        <span>info@velbrookendo.example</span>
      </div>
      <div class="row">
        <span class="spacer"></span>
        <span>www.velbrookendo.example</span>
      </div>
    </div>

    <div class="badge" role="img" aria-label="Certification member badge"></div>
  </section>
</main>
</body>
</html>
```